Lena Hartwell Web

Lena Hartwell is a singer/songwriter that has a presence in the market for over 20 years. She currently has a website, lenahartwell.example that needs a major makeover. IT needs to be reorganized to; 1) make it more user friendly; 2) enable multi-languages including; Spanish, French, Russian, Japanese, Chinese and Portuguese; 3) enable purchases online through a storefront of promotional merchandise and music tracks. She has a logo that needs an update, as well as we currently have a business card open on PixelBazaar for input. Working to re-brand, or refresh her brand.

Lena Hartwell is the next Rosa Delmont! She has 5 platinum records, Lumen Award nominations and tours with Harold Prescott globally and is Nora Vandermeer's key backup singer for 12 years.
Updates

Some common questions have come up.  Here is some further input:

1) Colors - No specific color in mind but probably earth tones.  Although at this point we''re completely open.  Mary likes classical style, Russian, French decor.  Paris architecture. Greek, Italian textures, Goddess like symbols from the Roman Empire, or the symbols and pomp of the British monarchy.  One name on tap for the new CD is "Lanterns Over Quiet Water"
2) Example website - I have not found a new one specifically, but what I don''t like about the existing one is it is not easy to navigate.  Needs to be streamlined and easy to navigate with a storefront for merchandise and music downloads.  
3) On Logo - We''re revamping a "Global" merchandise rollout logo.  We''ve also considered possibly modifying the old english "Hartwell" family crest which signifies royalty, but have not explored that too much.  The hexagon yellow logo on her current website, I was thinking of modifying to gold (brushed - or polished?), then taking the LH lettering using a fountain pen type look there the line thickness flows with pressure on the pen, then make the gold look like a pillow, with the letter making an impression into the gold pillow.  This expands to a high quality pin, blinged up broach with diamonds imbedded for example, Global label identity, tee shirts, label tag on fashion clothing etc etc. 
 4) One thing marketing has asked us to build is a routine video blog to reach out to fans in a personal way.  Short clips of daily activity, travel prep for shows, etc. Possibly a signup/fanpage where people get emails sent back whenever anything new is posted, like a video blog, new pics, new events.  A menu to choose what you get updates on. 

Thanks, Dennis

Target Market(s)

1) Fan base in Europe, Asia, Latin America and North America
2) Movie producers seeking soundtracks
3) Private clients seeking an outstanding performer for corporate events

Industry/Entity Type

Singer

Requirements
Must have
• Better organization into smaller pages. Items critical include: 1) music tracks, 2) ClipStream links, 3) photos & Video, 4) storefront to enable online merchandise purchase 5) a way to illustrate her genre from; gospel, to rock, funk, R&B, country,

```html
<!DOCTYPE html>
<html lang="en">
<head>
<meta charset="utf-8">
<title>Lena Hartwell – Official Site</title>
<link rel="stylesheet" href="https://fonts.googleapis.com/css2?family=Libre+Baskerville:wght@400;700&family=Open+Sans:wght@400;600&display=swap">
<style>
:root{
  --gold:#f1c40f;
  --gold-deep:#d9a400;
  --header:#383838;
  --bar:#3b3b3b;
  --panel:#ececec;
  --band:#e9e9e9;
  --text:#333;
  --muted:#777;
  --footer:#333;
  --footer-text:#d8d8d8;
  --serif:"Libre Baskerville", Georgia, serif;
  --sans:"Open Sans", Arial, sans-serif;
}
*{box-sizing:border-box;margin:0;padding:0}
html,body{width:970px;height:1200px;overflow:hidden}
body{position:relative;background:#fff;font-family:var(--sans);color:var(--text)}
a{color:inherit}
.abs{position:absolute}

/* header */
.topline{left:0;top:0;width:970px;height:6px;background:var(--gold)}
.site-header{left:0;top:6px;width:970px;height:65px;background:var(--header)}
.brand{left:97px;top:14px;font-family:var(--serif);font-weight:700;font-size:26px;color:var(--gold);letter-spacing:1px}
.main-nav{left:152px;top:26px;display:flex;font-family:var(--serif);font-size:12.4px;color:#fff;letter-spacing:.3px}
.main-nav span{padding:0 12px;border-left:1px solid #5a5a5a;line-height:13px}
.main-nav span:first-child{border-left:0;padding-left:3px}
.lang{left:840px;top:4px;width:33px;height:16px;background:#2c2c2c;border-radius:2px}
.lang i{position:absolute;left:6px;top:4px;width:13px;height:8px;background:#c9c9c9}
.lang b{position:absolute;left:23px;top:7px;border:3px solid transparent;border-top-color:#ccc}

/* hero */
.hero{left:0;top:71px;width:970px;height:359px;overflow:hidden;
  background:
   radial-gradient(ellipse 170px 200px at 440px 190px,#8a5a45 0%,rgba(120,80,60,0) 100%),
   radial-gradient(ellipse 260px 150px at 100px 60px,#5f8592 0%,rgba(95,133,146,0) 100%),
   linear-gradient(90deg,#5b3a22 0%,#9a5f2c 35%,#a8672e 60%,#c58a4a 85%,#d5a872 100%)}
.hero-name{left:756px;top:31px;width:214px;height:79px;background:rgba(230,220,205,.82);padding:14px 0 0 10px}
.hero-name h1{font-family:var(--serif);font-weight:400;font-style:normal;font-size:24px;color:#2b2b2b}
.hero-name p{font-size:10.5px;color:#333;margin-top:6px}
.arrow{top:160px}
.hero-strip{left:0;top:314px;width:970px;height:45px;background:rgba(215,210,205,.85);box-shadow:0 2px 3px rgba(0,0,0,.3)}
.quick{position:absolute;top:13px;display:flex;align-items:center;gap:6px;font-size:17px;color:#555;letter-spacing:.5px}
.quick i{display:inline-block;width:18px;height:18px;background:#555;border-radius:2px;position:relative}
.quick i::after{content:"";position:absolute;left:4px;top:4px;width:8px;height:8px;border-top:2px solid #fff;border-right:2px solid #fff}
.social{position:absolute;top:12px;display:flex;gap:6px;font-size:8.5px;color:#444;align-items:center}
.social span{display:flex;align-items:center;gap:3px}
.social i{width:13px;height:13px;background:#555;border-radius:2px;display:inline-block}

/* panels */
.panel{background:var(--panel)}
.panel-head{height:32px;background:var(--bar);color:#fff;font-family:var(--serif);font-size:12.5px;padding:10px 0 0 8px;position:relative;letter-spacing:.3px}
.open-icon{position:absolute;right:8px;top:7px;width:18px;height:18px;background:#c9c9c9;border-radius:3px}
.open-icon::after{content:"";position:absolute;left:5px;top:5px;width:6px;height:6px;border-top:2px solid #444;border-right:2px solid #444}
.more{position:absolute;right:0;bottom:0;background:#6b6b6b;color:#eee;font-size:8px;letter-spacing:.6px;padding:5px 7px}
.reply{display:inline-block;width:8px;height:6px;border-top:1.5px solid #888;border-right:1.5px solid #888;border-radius:0 4px 0 0;margin-left:4px}

.news{left:97px;top:453px;width:194px;height:426px}
.news ul{list-style:none;padding:12px 8px 0 3px}
.news li{display:flex;gap:7px;font-size:9.6px;line-height:11px;margin-bottom:11px}
.date{flex:0 0 23px;height:25px;background:var(--bar);color:#fff;text-align:center;font-size:7.5px;font-weight:600;line-height:9px;padding-top:2px}
.date b{display:block;font-size:11px;font-weight:400;line-height:12px}

.videos{left:304px;top:453px;width:360px;height:426px}
.video-frame{left:11px;top:47px;width:336px;height:220px;border-radius:9px;
  background:radial-gradient(ellipse 90px 120px at 240px 110px,#6e5a3c,rgba(0,0,0,0)),linear-gradient(120deg,#4a3a24,#7a6644 50%,#2e2418)}
.play{left:140px;top:88px;width:56px;height:42px;border-radius:8px;background:rgba(40,30,20,.75)}
.play::after{content:"";position:absolute;left:22px;top:12px;border:9px solid transparent;border-left:14px solid #fff;border-right:0}
.video-copy{left:12px;top:277px;width:336px;font-size:9.6px;line-height:11px}
.video-copy p{margin-bottom:6px}
.clip-tag{left:322px;top:273px;width:25px;height:25px;border-radius:5px;background:#555}

.store{left:677px;top:453px;width:194px;height:198px;border-bottom:6px solid var(--gold)}
.store .panel-head{background:var(--gold);color:#333}
.cart{position:absolute;right:8px;top:7px}
.store-name{position:absolute;left:20px;top:40px;width:154px;text-align:center;font-family:var(--serif);font-size:17px;color:#333;border-bottom:1px solid #555;padding-bottom:3px}
.seal{position:absolute;left:37px;top:72px;width:124px;height:104px;border-radius:50%;
  background:radial-gradient(circle at 50% 40%,#ffe25a,#e9b800 70%,#c99500);text-align:center;padding-top:30px;font-family:var(--serif)}
.seal b{display:block;font-size:22px;color:#c58d00;font-weight:700;letter-spacing:.5px}
.seal span{font-size:10px;color:#5a4300}

.tweets{left:677px;top:664px;width:194px;height:234px}
.tweets ul{list-style:none;padding:12px 6px 0 0}
.tweets li{display:flex;gap:8px;font-size:9.6px;line-height:11px;margin-bottom:14px}
.tweets li i{flex:0 0 25px;height:25px;background:#555;border-radius:1px}

/* gallery */
.gallery{left:0;top:912px;width:970px;height:134px;background:var(--band)}
.gallery h2{position:absolute;left:97px;top:11px;font-family:var(--serif);font-weight:400;font-size:10.5px;color:#222;display:flex;align-items:center;gap:6px}
.gallery h2 i{width:13px;height:10px;background:#333;border-radius:2px}
.gallery .open-icon{top:8px;right:99px;width:12px;height:12px;background:#555}
.gallery .open-icon::after{left:3px;top:3px;width:4px;height:4px;border-color:#fff;border-width:1.5px}
.shot{position:absolute;top:23px;height:97px}

/* footer */
.site-footer{left:0;top:1046px;width:970px;height:147px;background:var(--footer);color:var(--footer-text)}
.bottomline{left:0;top:1193px;width:970px;height:7px;background:var(--gold)}
.fcol{position:absolute;top:17px;font-size:9.5px}
.fcol h3{font-weight:400;font-size:9.5px;margin-bottom:9px}
.fcol ul{list-style:none}
.fcol li{font-size:7.6px;line-height:13.7px;padding-left:3px}
.fcol li a{text-decoration:underline}
.divider{position:absolute;top:22px;width:1px;height:115px;background:#555}
.soc li{display:flex;align-items:center;gap:5px;line-height:19.5px}
.soc i{width:12px;height:12px;background:#777;border-radius:2px}
.copy{display:flex;align-items:center;gap:6px;font-size:9.5px}
.copy i{width:25px;height:25px;border-radius:50%;background:#c9a400}
</style>
</head>
<body>

<div class="abs topline"></div>
<header class="abs site-header">
  <div class="abs brand">LH</div>
  <nav class="abs main-nav">
    <span>HOME</span><span>EVENTS</span><span>MUSIC</span><span>VIDEO</span><span>PICTURES</span><span>ABOUT</span><span>ONLINE STORE</span><span>CONTACT</span>
  </nav>
  <div class="abs lang" aria-label="Language selector"><i></i><b></b></div>
</header>

<section class="abs hero" role="img" aria-label="Portrait photograph of Lena Hartwell seated in a car with tan leather seats, wearing a fur collar">
  <div class="abs hero-name">
    <h1>Lena Hartwell</h1>
    <p>Award winning Singer/Songwriter</p>
  </div>
  <svg class="abs arrow" style="left:25px" width="26" height="40" viewBox="0 0 26 40"><polyline points="22,2 4,20 22,38" fill="none" stroke="#d9d9d9" stroke-width="4"/></svg>
  <svg class="abs arrow" style="left:920px" width="26" height="40" viewBox="0 0 26 40"><polyline points="4,2 22,20 4,38" fill="none" stroke="#d9d9d9" stroke-width="4"/></svg>
  <div class="abs hero-strip">
    <div class="quick" style="left:97px">STORE <i></i></div>
    <div class="quick" style="left:214px">MUSIC <i></i></div>
    <div class="quick" style="left:333px">VIDEO <i></i></div>
    <div class="social" style="left:737px">
      <span><i></i>FaceLoop</span><span><i></i>Chirper</span><span><i></i>ClipStream</span>
    </div>
  </div>
</section>

<section class="abs panel news">
  <div class="panel-head">LATEST NEWS<span class="open-icon"></span></div>
  <ul>
    <li><div class="date">NOV<b>12</b></div><p>Curabitur nisi purus, mattis sit amet aliquet nec, vehicula a lorem. Nulla aliquet ac felis non interdum. Sed et dapibus est, in luctus quam ....<span class="reply"></span></p></li>
    <li><div class="date">NOV<b>14</b></div><p>Nullam volutpat enim sed justo ultricies ultrices. Aliquam aliquam quam nec est egestas aliquet. Suspendisse ornare et quam sit amet euismod ...<span class="reply"></span></p></li>
    <li><div class="date">NOV<b>27</b></div><p>Suspendisse eget eleifend quam. Aliquam pellentesque hendrerit quam id sollicitudin. Nulla id justo massa ...<span class="reply"></span></p></li>
    <li><div class="date">DEC<b>5</b></div><p>Sed accumsan tortor arcu, eu iaculis enim luctus sit amet. Curabitur cursus semper ....<span class="reply"></span></p></li>
    <li><div class="date">DEC<b>14</b></div><p>Praesent tincidunt vulputate enim ac tincidunt. Etiam tristique metus a commodo volutpat. Aliquam at luctus velit. Quisque elementum suscipit mauris a tincidunt ....<span class="reply"></span></p></li>
    <li><div class="date">DEC<b>22</b></div><p>Etiam tristique metus a commodo volutpat. Aliquam at luctus velit. Quisque elementum suscipit mauris a tincidunt.<span class="reply"></span></p></li>
  </ul>
  <span class="more">MORE &gt;&gt;</span>
</section>

<section class="abs panel videos">
  <div class="panel-head">VIDEOS<span class="open-icon"></span></div>
  <div class="abs video-frame" role="img" aria-label="Video still of Lena Hartwell singing on stage beside a microphone stand, warm sepia stage lights">
    <div class="abs play"></div>
  </div>
  <div class="abs clip-tag"></div>
  <div class="abs video-copy">
    <p style="width:300px">Praesent tincidunt vulputate enim ac tincidunt. Etiam tristique metus a commodo volutpat. Aliquam at luctus velit.</p>
    <p style="margin-top:10px">Quisque elementum suscipit mauris a tincidunt. Pellentesque fermentum vehicula dui vitae tristique. Aenean in urna lacinia, imperdiet nulla ut, elementum quam. Aliquam dignissim erat in urna accumsan, in vehicula tortor vestibulum.<br>Cras molestie ante nec magna suscipit, quis accumsan neque consectetur. Praesent iaculis massa arcu, quis molestie risus lobortis non. Vivamus sed lectus ac velit vulputate iaculis. Nunc nulla elit, lobortis at mauris vitae, tristique pulvinar lectus.</p>
  </div>
  <span class="more">MORE &gt;&gt;</span>
</section>

<section class="abs panel store">
  <div class="panel-head">ONLINE STORE
    <svg class="cart" width="22" height="18" viewBox="0 0 22 18"><path d="M0 2h4l3 9h11l3-7H6" fill="none" stroke="#333" stroke-width="2.2"/><circle cx="8" cy="15" r="2" fill="#333"/><circle cx="17" cy="15" r="2" fill="#333"/></svg>
  </div>
  <div class="store-name">Lena Hartwell</div>
  <div class="seal"><b>STORE</b><span>NOW OPEN</span></div>
</section>

<section class="abs panel tweets">
  <div class="panel-head">CHIRPER<span class="open-icon"></span></div>
  <ul>
    <li><i></i><p>Etiam tristique metus a commodo volutpat. Aliquam at luctus velit. Quisque elementum suscipit mauris a tincidunt ...<span class="reply"></span></p></li>
    <li><i></i><p>Pellentesque fermentum vehicula dui vitae tristique. Aenean in urna lacinia, imperdiet nulla ut, elementum quam ...<span class="reply"></span></p></li>
    <li><i></i><p>Aliquam dignissim erat in urna accumsan, in vehicula tortor vestibulum. Cras molestie ante nec magna suscipit ...<span class="reply"></span></p></li>
  </ul>
  <span class="more">MORE &gt;&gt;</span>
</section>

<section class="abs gallery">
  <h2><i></i>PHOTO GALLERY</h2>
  <span class="open-icon"></span>
  <svg class="abs" style="left:68px;top:59px" width="16" height="26" viewBox="0 0 16 26"><polyline points="14,2 3,13 14,24" fill="none" stroke="#bbb" stroke-width="3"/></svg>
  <svg class="abs" style="left:884px;top:59px" width="16" height="26" viewBox="0 0 16 26"><polyline points="2,2 13,13 2,24" fill="none" stroke="#bbb" stroke-width="3"/></svg>
  <div class="shot" style="left:97px;width:144px;background:linear-gradient(135deg,#c98a8f,#8a4f55 60%,#e2d5d6)" role="img" aria-label="Photo of the singer in a recording studio"></div>
  <div class="shot" style="left:244px;width:64px;background:linear-gradient(160deg,#d8d8d8,#666 55%,#333)" role="img" aria-label="Black and white concert photo"></div>
  <div class="shot" style="left:310px;width:144px;background:linear-gradient(120deg,#2e2a28,#7a4a3e 50%,#1e1a18)" role="img" aria-label="Photo of two performers singing on stage"></div>
  <div class="shot" style="left:457px;width:106px;background:linear-gradient(150deg,#a6bcc8,#4e6470 60%,#7c8f99)" role="img" aria-label="Blue toned portrait photo"></div>
  <div class="shot" style="left:567px;width:81px;background:linear-gradient(170deg,#3a3030,#a07878 55%,#d5a6b4)" role="img" aria-label="Concert photo with audience"></div>
  <div class="shot" style="left:651px;width:72px;background:linear-gradient(160deg,#3b3f9a,#7a6ec0 50%,#c7b6d6)" role="img" aria-label="Stage photo under blue light"></div>
  <div class="shot" style="left:726px;width:145px;background:linear-gradient(120deg,#4a3e6a,#9a7fa8 55%,#d8c6d8)" role="img" aria-label="Close-up stage photo with microphone"></div>
</section>

<footer class="abs site-footer">
  <div class="fcol" style="left:100px;top:16px">
    <div class="copy"><i></i>Lena Hartwell 2014</div>
  </div>
  <span class="divider" style="left:293px"></span>
  <div class="fcol" style="left:314px">
    <h3>Quick Nav</h3>
    <ul><li><a>Home</a></li><li><a>Events</a></li><li><a>Music</a></li><li><a>Video</a></li><li><a>Pictures</a></li><li><a>About</a></li><li><a>Online Store</a></li><li><a>Contact</a></li></ul>
  </div>
  <span class="divider" style="left:463px"></span>
  <div class="fcol soc" style="left:483px">
    <h3>Social networking</h3>
    <ul>
      <li><i></i>Lena Hartwell on <a>FaceLoop</a></li>
      <li><i></i>Lena Hartwell on <a>Chirper</a></li>
      <li><i></i>Lena Hartwell on <a>ClipStream</a></li>
      <li><i></i>Lena Hartwell on <a>RSS</a></li>
    </ul>
  </div>
  <span class="divider" style="left:680px"></span>
  <div class="fcol soc" style="left:700px">
    <h3>Quick Contact</h3>
    <ul>
      <li><svg width="12" height="12" viewBox="0 0 12 12"><circle cx="6" cy="3.5" r="3" fill="#999"/><path d="M1 12c0-4 10-4 10 0z" fill="#999"/></svg>Lena Hartwell</li>
      <li><svg width="12" height="10" viewBox="0 0 12 10"><rect x="0.5" y="0.5" width="11" height="9" fill="#999"/><polyline points="0.5,0.5 6,5.5 11.5,0.5" fill="none" stroke="#333"/></svg><a>contact@lenahartwell.example</a></li>
    </ul>
  </div>
</footer>
<div class="abs bottomline"></div>

</body>
</html>
```